Advertisements for dental office (3"x3.75" and 3"x2")
People of all ages looking for a family dentist.
I am looking for advertisements that are clean and sophisticated. Most dental ads are cluttered looking and list all the procedures that a dentist will perform. I do not want clutter. I want an ad that speaks for itself and has a lot of emotional appeal. The ads should be simple but still catch your eye.

```html
<!DOCTYPE html>
<html lang="en">
<head>
<meta charset="utf-8">
<title>Dental Office Advertisements</title>
<link rel="stylesheet" href="https://fonts.googleapis.com/css2?family=Open+Sans:ital,wght@0,400;0,600;0,700;1,400&family=Cinzel:wght@500&display=swap">
<style>
  :root {
    --plum: #6a2141;
    --plum-dark: #4f1530;
    --plum-soft: #a5617e;
    --white: #ffffff;
    --ink: #3b2a33;
    --mist: #e9e6e8;
    --stage: #d9d4cf;
    --photo-top: #d8c3b3;
    --photo-mid: #c9977e;
    --photo-low: #3f6fb4;
  }
  * { box-sizing: border-box; margin: 0; padding: 0; }
  html, body { width: 1200px; height: 626px; overflow: hidden; }
  body {
    background: var(--stage);
    font-family: "Open Sans", Arial, sans-serif;
    color: var(--ink);
    position: relative;
  }
  .ad {
    position: absolute;
    top: 108px;
    height: 403px;
    background: linear-gradient(160deg, var(--white) 55%, var(--mist) 100%);
    overflow: hidden;
    box-shadow: 0 6px 18px rgba(0,0,0,0.25);
  }
  .ad--wide { left: 204px; width: 492px; }
  .ad--tall { left: 732px; width: 264px; }

  .ad__band { position: absolute; left: 0; top: 0; width: 100%; z-index: 2; }
  .ad__headline {
    position: absolute; z-index: 3; right: 18px; text-align: right; color: var(--white);
  }
  .ad__title { font-weight: 700; line-height: 1.1; }
  .ad__subtitle { font-weight: 400; line-height: 1.2; }
  .ad__quote { font-style: italic; line-height: 1.3; }

  .ad--wide .ad__headline { top: 14px; }
  .ad--wide .ad__title { font-size: 27px; }
  .ad--wide .ad__subtitle { font-size: 21px; }
  .ad--wide .ad__quote { font-size: 11px; margin-top: 2px; }

  .ad--tall .ad__headline { top: 12px; right: 12px; }
  .ad--tall .ad__title { font-size: 20px; }
  .ad--tall .ad__subtitle { font-size: 14px; }
  .ad--tall .ad__quote { font-size: 8.5px; margin-top: 1px; }

  .ad__photo {
    position: absolute; z-index: 1;
    background: linear-gradient(180deg, var(--photo-top) 0%, var(--photo-mid) 45%, var(--photo-low) 80%);
  }
  .ad--wide .ad__photo { left: 0; top: 90px; width: 290px; height: 313px; }
  .ad--tall .ad__photo { left: 0; top: 90px; width: 264px; height: 250px; }

  .brand { display: flex; flex-direction: column; align-items: center; }
  .brand__mark { width: 22px; height: 22px; border-radius: 50%; background: var(--plum); }
  .brand__name { font-family: "Cinzel", Georgia, serif; font-weight: 500; color: var(--plum); white-space: nowrap; }
  .brand__tagline { color: var(--plum-soft); white-space: nowrap; }

  .ad--wide .ad__details {
    position: absolute; left: 290px; top: 150px; width: 202px;
    display: flex; flex-direction: column; align-items: center; z-index: 3;
  }
  .ad--wide .brand__mark { margin-bottom: 8px; }
  .ad--wide .brand__name { font-size: 12px; }
  .ad--wide .brand__tagline { font-size: 7px; margin-top: 3px; }
  .ad--wide .contact { margin-top: 38px; align-self: flex-end; margin-right: 22px; text-align: right; font-size: 13.5px; line-height: 1.35; color: var(--ink); }

  .ad__footer { position: absolute; left: 0; bottom: 0; width: 100%; z-index: 2; }
  .ad--tall .ad__details {
    position: absolute; left: 0; bottom: 12px; width: 100%; z-index: 3;
    display: flex; justify-content: space-between; align-items: flex-end; padding: 0 12px;
  }
  .ad--tall .brand__mark { width: 14px; height: 14px; margin-bottom: 4px; }
  .ad--tall .brand__name { font-size: 7.5px; }
  .ad--tall .contact { text-align: right; font-size: 8px; line-height: 1.35; }
</style>
</head>
<body>

<section class="ad ad--wide">
  <svg class="ad__band" viewBox="0 0 492 130" width="492" height="130" aria-hidden="true">
    <path d="M0 0H492V88C380 118 200 128 0 110Z" fill="var(--plum)"/>
    <path d="M0 114C200 132 380 122 492 92" fill="none" stroke="var(--plum-soft)" stroke-width="2"/>
  </svg>
  <div class="ad__headline">
    <p class="ad__title">A Beautiful Smile</p>
    <p class="ad__subtitle">Today, It's Easier Than Ever</p>
    <p class="ad__quote">"Comprehensive Dentistry For All Ages"</p>
  </div>
  <div class="ad__photo" role="img" aria-label="Photo of a smiling older couple embracing"></div>
  <div class="ad__details">
    <div class="brand">
      <span class="brand__mark"></span>
      <span class="brand__name">Marcus T. Revin, DDS, PLLC</span>
      <span class="brand__tagline">Family &amp; Cosmetic Dentistry</span>
    </div>
    <address class="contact" style="font-style:normal">
      218 West Alder Street<br>Brookhaven<br>555-014-2736
    </address>
  </div>
</section>

<section class="ad ad--tall">
  <svg class="ad__band" viewBox="0 0 264 110" width="264" height="110" aria-hidden="true">
    <path d="M0 0H264V84C190 104 100 108 0 98Z" fill="var(--plum)"/>
  </svg>
  <div class="ad__headline">
    <p class="ad__title">A Beautiful Smile</p>
    <p class="ad__subtitle">Today, It's Easier Than Ever</p>
    <p class="ad__quote">"Comprehensive Dentistry For All Ages"</p>
  </div>
  <div class="ad__photo" role="img" aria-label="Photo of a smiling older couple embracing"></div>
  <svg class="ad__footer" viewBox="0 0 264 80" width="264" height="80" aria-hidden="true">
    <path d="M0 20C90 0 180 4 264 22V80H0Z" fill="var(--white)"/>
    <path d="M0 16C90 -4 180 0 264 18" fill="none" stroke="var(--plum)" stroke-width="3"/>
  </svg>
  <div class="ad__details">
    <div class="brand">
      <span class="brand__mark"></span>
      <span class="brand__name">Marcus T. Revin, DDS, PLLC</span>
    </div>
    <address class="contact" style="font-style:normal">
      218 West Alder Street<br>Brookhaven<br>555-014-2736
    </address>
  </div>
</section>

</body>
</html>
```